Coffee and hot drinks advert on A-Board

Creative eye catching design to advertise coffee and hot drinks on an A-Board.

To use images and modern design to reflect the quality and almost specialist coffee house style drinks on offer.
We use organic milk and have had our own 'Larkfield Restaurant' coffee beans roasted to produce the perfect coffee.
We also use only the best hot chocolate and fresh cream to serve quality drinks.
All staff are barista trained.

Target Market(s)

Passing trade and coffee lovers for takeaway drinks

Industry/Entity Type

Coffee Shop

Font styles to use
Serif

Requirements
Must have
• Bold creative modern look.
• Independent coffee shop style look
• Mention we use 'Bramblewick Organic milk'
• We use our own roasted special blend of coffee
• speciality hot chocolate
Nice to have
• modern approach
• eye catching
Should not have
• complicated
• difficult to read
• old fashioned

```html
<!DOCTYPE html>
<html lang="en">
<head>
<meta charset="utf-8">
<title>Specialty Coffee Roasters – A-Board</title>
<link rel="stylesheet" href="https://fonts.googleapis.com/css2?family=Anton&family=Oswald:wght@600;700&family=Lato:wght@400&family=Tinos:wght@400;700&display=swap">
<style>
  :root {
    --board-black: #050404;
    --board-dark: #1b1412;
    --title-yellow: #f3ee86;
    --text-white: #ffffff;
    --highlight-cream: #f6ef9c;
    --badge-red: #7c1a10;
    --badge-ring: #ffffff;
    --badge-text: #ffe600;
    --bean-dark: #2a1408;
    --bean-mid: #6b3514;
    --bean-light: #a8592a;
  }
  * { margin: 0; padding: 0; box-sizing: border-box; }
  html, body {
    width: 852px; height: 1200px; overflow: hidden;
    background: var(--board-black);
  }
  .board {
    position: relative; width: 852px; height: 1200px; overflow: hidden;
    background: radial-gradient(ellipse 70% 40% at 50% 42%, var(--board-dark) 0%, var(--board-black) 70%);
    color: var(--text-white);
  }
  .brand-title {
    position: absolute; top: 62px; left: 0; width: 100%;
    text-align: center;
    font-family: "Oswald", sans-serif; font-weight: 700;
    font-size: 58px; line-height: 1; color: var(--title-yellow);
    letter-spacing: 0.5px;
  }
  .brand-tagline {
    position: absolute; top: 150px; left: 0; width: 100%;
    text-align: center;
    font-family: "Lato", sans-serif; font-size: 27px; color: var(--title-yellow);
  }
  .photo-strip {
    position: absolute; top: 219px; left: 68px; width: 714px; height: 88px;
    display: flex; gap: 6px;
  }
  .photo-strip .tile { flex: 1; height: 100%; }
  .tile--cake { background: linear-gradient(135deg, #3b2216, #c9a47a 60%, #e8dccb); }
  .tile--beans { background: linear-gradient(135deg, #4a2a16, #7a4a2a 50%, #2a160b); }
  .tile--latte { background: radial-gradient(circle at 50% 50%, #e9c99a 0%, #b8743c 45%, #5a3018 90%); }
  .tile--cup { background: radial-gradient(circle at 45% 50%, #1a0e08 0%, #3b2418 30%, #d8d2cc 40%, #6b4a32 75%); }
  .tile--spice { background: linear-gradient(135deg, #5a3520, #a0602e 50%, #3a2012); }
  .headline {
    position: absolute; top: 358px; left: 0; width: 100%;
    text-align: center;
    font-family: "Anton", sans-serif; font-weight: 400;
    font-size: 120px; line-height: 1.0; color: var(--text-white);
    letter-spacing: 0.5px;
  }
  .beans-photo {
    position: absolute; left: 0; bottom: 0; width: 852px; height: 370px;
    background:
      radial-gradient(ellipse 60% 45% at 40% 100%, var(--bean-light) 0%, transparent 70%),
      radial-gradient(ellipse 80% 60% at 50% 100%, var(--bean-mid) 0%, var(--bean-dark) 60%, transparent 100%);
  }
  .selling-points {
    position: absolute; top: 596px; left: 76px; list-style: none;
    font-family: "Tinos", serif; font-size: 27px; line-height: 34px;
    color: var(--text-white);
  }
  .selling-points li { margin-bottom: 31px; }
  .selling-points li::before { content: "\2022"; color: var(--title-yellow); margin-right: 8px; }
  .selling-points .house-blend { font-weight: 700; color: var(--highlight-cream); }
  .promise-badge {
    position: absolute; left: 508px; top: 751px; width: 308px; height: 308px;
  }
  .promise-badge__text {
    position: absolute; inset: 0;
    display: flex; align-items: center; justify-content: center; text-align: center;
    font-family: "Oswald", sans-serif; font-weight: 600;
    font-size: 40px; line-height: 46px; color: var(--badge-text);
  }
</style>
</head>
<body>
<main class="board">
  <h1 class="brand-title">Specialty Coffee Roasters</h1>
  <p class="brand-tagline">Producing Slow Roasted Coffee &amp; Hot Drinks</p>

  <div class="photo-strip">
    <div class="tile tile--cake" role="img" aria-label="Photo of a slice of cake with a cup of coffee"></div>
    <div class="tile tile--beans" role="img" aria-label="Photo of ground coffee on a spoon"></div>
    <div class="tile tile--latte" role="img" aria-label="Photo of latte art in a cup"></div>
    <div class="tile tile--cup" role="img" aria-label="Photo of a black coffee seen from above"></div>
    <div class="tile tile--spice" role="img" aria-label="Photo of cinnamon sticks and coffee"></div>
  </div>

  <h2 class="headline">Take away the<br>ultimate coffee</h2>

  <div class="beans-photo" role="img" aria-label="Photo of a heap of roasted coffee beans"></div>

  <ul class="selling-points">
    <li>Try our own <span class="house-blend">'Larkfield Restaurant'</span> roasted<br>coffee beans with Bramblewick organic milk<br>to produce the perfect coffee.</li>
    <li>Discover the ultimate speciality<br>hot chocolate with fresh cream.</li>
    <li>All staff<br>are barista<br>trained.</li>
  </ul>

  <div class="promise-badge">
    <svg width="308" height="308" viewBox="0 0 308 308" aria-hidden="true">
      <circle cx="154" cy="154" r="152" fill="var(--badge-ring)"/>
      <circle cx="160" cy="154" r="132" fill="var(--badge-red)"/>
    </svg>
    <p class="promise-badge__text">We make<br>it the way<br>you like it!</p>
  </div>
</main>
</body>
</html>
```